Layout for site fence advertising - length approx. 250 cm x 125 cm

The advertising will later be printed on a PVC film and used for events or on sports fields.

Main services :
Your regional contact at
Real estate and business financing
independent insurance advice

```html
<!DOCTYPE html>
<html lang="de">
<head>
<meta charset="utf-8">
<title>Nordwert Vermögensberatung – Bauzaunbanner</title>
<link rel="stylesheet" href="https://fonts.googleapis.com/css2?family=Fira+Sans:wght@400&family=Inter:wght@900&family=Montserrat:wght@700&display=swap">
<style>
  :root {
    --brand-blue: #1b59b9;
    --text-grey: #5e5e5e;
    --paper: #ffffff;
    --portrait-light: #d9b9a6;
    --portrait-dark: #2a2835;
  }
  html, body {
    margin: 0;
    padding: 0;
    width: 1200px;
    height: 600px;
    overflow: hidden;
    background: var(--paper);
  }
  .banner {
    position: relative;
    width: 1200px;
    height: 600px;
    overflow: hidden;
    background: var(--paper);
  }
  .banner__wave {
    position: absolute;
    inset: 0;
    width: 1200px;
    height: 600px;
  }
  .banner__title {
    position: absolute;
    left: 72px;
    top: 46px;
    margin: 0;
    font-family: "Inter", sans-serif;
    font-weight: 900;
    font-size: 67px;
    letter-spacing: -0.5px;
    color: var(--paper);
    line-height: 1;
  }
  .services {
    position: absolute;
    left: 73px;
    top: 196px;
    margin: 0;
    padding: 0;
    list-style: none;
  }
  .services__item {
    display: flex;
    align-items: center;
    height: 52px;
    font-family: "Fira Sans", sans-serif;
    font-weight: 400;
    font-size: 32px;
    letter-spacing: 0.8px;
    color: var(--text-grey);
    white-space: nowrap;
  }
  .services__tick {
    width: 40px;
    height: 52px;
    margin-right: 6px;
    flex: none;
  }
  .banner__rule {
    position: absolute;
    left: 13px;
    top: 372px;
    width: 880px;
    height: 3px;
    background: var(--brand-blue);
  }
  .brand {
    position: absolute;
    left: 62px;
    top: 400px;
    height: 170px;
    display: flex;
    align-items: center;
  }
  .brand__mark {
    width: 166px;
    height: 166px;
    flex: none;
  }
  .brand__divider {
    width: 4px;
    height: 170px;
    margin: 0 12px 0 17px;
    background: var(--text-grey);
  }
  .brand__text {
    margin-top: -28px;
    white-space: nowrap;
  }
  .brand__name {
    margin: 0;
    font-family: "Montserrat", sans-serif;
    font-weight: 700;
    font-size: 25px;
    color: var(--brand-blue);
    line-height: 1.1;
  }
  .brand__tagline {
    margin: 10px 0 0;
    font-family: "Montserrat", sans-serif;
    font-weight: 700;
    font-size: 22px;
    color: var(--text-grey);
    line-height: 1.1;
  }
  .portrait {
    position: absolute;
    left: 840px;
    top: 52px;
    width: 360px;
    height: 548px;
    border-radius: 180px 180px 0 0;
    background: linear-gradient(180deg, var(--portrait-light) 0%, #c99f8a 45%, #e9e8ee 58%, var(--portrait-dark) 72%, var(--portrait-dark) 100%);
  }
</style>
</head>
<body>
<main class="banner">
  <svg class="banner__wave" viewBox="0 0 1200 600" aria-hidden="true">
    <path d="M0,0 H1200 V196 C1120,236 960,258 860,248 C700,232 520,172 360,158 C200,146 60,150 0,182 Z" fill="var(--brand-blue)"/>
  </svg>

  <h1 class="banner__title">HAUPTLEISTUNGEN :</h1>

  <ul class="services">
    <li class="services__item">
      <svg class="services__tick" viewBox="0 0 40 52" aria-hidden="true">
        <rect x="1.5" y="17.5" width="30" height="30" fill="none" stroke="var(--text-grey)" stroke-width="2.5"/>
        <path d="M8,19 L16,40 L38,3" fill="none" stroke="var(--brand-blue)" stroke-width="4.5" stroke-linecap="round" stroke-linejoin="round"/>
      </svg>
      Ihr regionaler Kontakt unter
    </li>
    <li class="services__item">
      <svg class="services__tick" viewBox="0 0 40 52" aria-hidden="true">
        <rect x="1.5" y="17.5" width="30" height="30" fill="none" stroke="var(--text-grey)" stroke-width="2.5"/>
        <path d="M8,19 L16,40 L38,3" fill="none" stroke="var(--brand-blue)" stroke-width="4.5" stroke-linecap="round" stroke-linejoin="round"/>
      </svg>
      Immobilien- und Betriebsfinanzierung
    </li>
    <li class="services__item">
      <svg class="services__tick" viewBox="0 0 40 52" aria-hidden="true">
        <rect x="1.5" y="17.5" width="30" height="30" fill="none" stroke="var(--text-grey)" stroke-width="2.5"/>
        <path d="M8,19 L16,40 L38,3" fill="none" stroke="var(--brand-blue)" stroke-width="4.5" stroke-linecap="round" stroke-linejoin="round"/>
      </svg>
      Unabhängiger Versicherungsratgeber
    </li>
  </ul>

  <div class="banner__rule"></div>

  <div class="brand">
    <svg class="brand__mark" viewBox="0 0 166 166" aria-hidden="true">
      <circle cx="83" cy="83" r="79" fill="none" stroke="var(--brand-blue)" stroke-width="6"/>
    </svg>
    <div class="brand__divider"></div>
    <div class="brand__text">
      <p class="brand__name">Nordwert Vermögensberatung GmbH</p>
      <p class="brand__tagline">Finanzieren, Versichern, Vorsorgen</p>
    </div>
  </div>

  <div class="portrait" role="img" aria-label="Porträtfoto des Beraters in dunklem Sakko und weißem Hemd"></div>
</main>
</body>
</html>
```